Corvel Power renewable energy company Website design

Re-design our current website www.corvelpower.com.au. Products and packages need updating which we can provide. Just looking for a change from our tired website. Would like to add a blog section to the website along with EV Chargers section. Need to add our QLD electrical contractors licence number to each footer on every page. Need to keep the get a quote form fill section.

Target Market(s)

Home owners looking for renewable energy options

Industry/Entity Type

Renewable Energy

Coding

Coded - Design and coding required

Number of Pages Required

5+ page

Requirements
Nice to have
• We do like a website that flows and has movement. In a way directing the consumers eyes to which ever section we want highlighted.

```html
<!DOCTYPE html>
<html lang="en">
<head>
<meta charset="utf-8">
<title>Corvel Power — Solar Power Solutions</title>
<link href="https://fonts.googleapis.com/css2?family=Red+Hat+Display:wght@400;500;700;900&display=swap" rel="stylesheet">
<style>
:root{
  --navy:#1c2343;
  --navy-deep:#141a33;
  --red:#d3142b;
  --charcoal:#2e3238;
  --ink:#1d1f24;
  --muted:#6b6f78;
  --light:#f1f1f3;
  --white:#ffffff;
}
*{box-sizing:border-box;margin:0;padding:0}
html,body{width:1200px;height:4688px;overflow:hidden}
body{font-family:"Red Hat Display",Arial,sans-serif;color:var(--ink);background:var(--white)}
.section{position:relative;width:1200px;overflow:hidden}
.wrap{position:relative;width:1000px;margin:0 auto;z-index:2}
.wave{position:absolute;left:0;bottom:0;width:1200px;z-index:1}
.btn{display:inline-block;background:var(--red);color:var(--white);font-size:13px;font-weight:700;padding:11px 24px;border-radius:3px}
.btn-outline{display:inline-block;border:1px solid #c9c9ce;color:var(--ink);font-size:13px;font-weight:500;padding:9px 20px}
.eyebrow{color:var(--red);font-size:15px;font-weight:700;margin-bottom:10px}
.brand{color:var(--white);font-weight:900;font-size:20px;letter-spacing:.5px;display:flex;align-items:center;gap:10px}
.brand-square{width:26px;height:26px;background:var(--red)}
p{font-size:14px;line-height:1.7;color:var(--muted)}

/* hero */
.hero{height:900px;background:var(--navy)}
.hero-photo{position:absolute;inset:0;background:linear-gradient(160deg,#2b3556 0%,#3e4a63 40%,#6d6a66 70%,#2a2f3e 100%)}
.hero-photo::after{content:"";position:absolute;inset:0;background:linear-gradient(90deg,rgba(20,26,51,.85) 0%,rgba(20,26,51,.35) 65%,rgba(20,26,51,.1) 100%)}
.nav{display:flex;align-items:center;justify-content:space-between;padding-top:34px}
.nav-links{display:flex;gap:26px;align-items:center;color:var(--white);font-size:13px;font-weight:500}
.hero-copy{margin-top:220px;width:560px}
.hero-copy .tag{color:var(--white);font-size:20px;font-weight:700;margin-bottom:14px}
.hero-copy .tag span{color:var(--red)}
.hero-copy h1{color:var(--white);font-size:58px;line-height:1.1;font-weight:700;margin-bottom:34px}
.hero-dots{position:absolute;right:0;top:330px;display:flex;flex-direction:column;gap:10px}
.hero-dots i{display:block;width:10px;height:10px;border:2px solid var(--white);border-radius:50%}
.hero-dots i.on{background:var(--white)}

/* about */
.about{height:300px;padding-top:20px}
.about .wrap{display:flex;gap:60px;align-items:flex-start}
.about-photo{width:380px;height:260px;background:linear-gradient(180deg,#8ec1e6 0%,#b9d6ea 45%,#c77a5a 75%,#d9d3c6 100%)}
.about-copy{width:520px;padding-top:14px}
.about-copy h2{font-size:34px;line-height:1.15;font-weight:700;margin-bottom:14px}
.about-copy .link{margin-top:16px;font-size:13px;font-weight:700;border:1px solid #c9c9ce;display:inline-block;padding:8px 16px}

/* difference */
.difference{height:400px;background:var(--navy);padding-top:42px}
.difference h3{color:var(--white);font-size:16px;font-weight:700;margin-bottom:44px}
.diff-row{display:flex;justify-content:space-between}
.diff-item{width:180px;text-align:center;color:var(--white);font-size:13px;line-height:1.5}
.diff-item svg{display:block;margin:0 auto 14px}
.diff-mark{position:absolute;left:50%;top:255px;transform:translateX(-50%);width:44px;height:44px;border:2px solid var(--white);background:var(--red);z-index:3}

/* ev */
.ev{height:420px;background:var(--light);padding-top:50px}
.ev .wrap{display:flex;justify-content:space-between}
.ev-copy{width:480px;padding-top:30px}
.ev-copy h2{font-size:34px;line-height:1.2;font-weight:700;margin-bottom:16px}
.ev-copy .btn-outline{margin-top:20px}
.ev-photo{width:440px;height:310px;background:linear-gradient(170deg,#d7dade 0%,#9ea7ac 50%,#5c6b62 100%)}

/* packages */
.packages{height:620px;padding-top:70px}
.pkg-head{display:flex;justify-content:space-between;align-items:center;margin-bottom:40px}
.pkg-head h2{font-size:30px;font-weight:700}
.pkg-row{display:flex;justify-content:space-between}
.pkg{position:relative;width:300px;height:400px;text-align:center}
.pkg svg.house{position:absolute;inset:0}
.pkg-img{position:absolute;left:80px;top:90px;width:140px;height:110px;background:linear-gradient(180deg,#c9d1dd 0%,#3a4764 100%)}
.pkg-price{position:absolute;left:112px;top:178px;width:76px;height:76px;background:var(--red);transform:rotate(45deg);display:flex;align-items:center;justify-content:center}
.pkg-price span{transform:rotate(-45deg);color:var(--white);font-weight:900;font-size:17px;line-height:1.1}
.pkg-info{position:absolute;left:0;right:0;top:276px;font-size:13px}
.pkg-info b{display:block;font-size:14px;margin-bottom:6px}
.pkg-info .was{color:var(--red);font-weight:700;margin-top:8px;display:block}
.pkg-info .btn-outline{margin-top:14px;font-size:12px;padding:7px 16px}

/* savings */
.savings{height:660px;background:var(--charcoal);padding-top:60px;text-align:center}
.savings h2{color:var(--white);font-size:36px;font-weight:700;margin-bottom:18px}
.savings p{color:#b9bcc4;width:860px;margin:0 auto}
.save-grid{position:relative;width:640px;margin:40px auto 0;display:grid;grid-template-columns:1fr 1fr;row-gap:40px}
.save-grid::before{content:"";position:absolute;left:50%;top:0;bottom:0;border-left:1px solid #5a5f68}
.save-grid::after{content:"";position:absolute;top:50%;left:0;right:0;border-top:1px solid #5a5f68}
.save-item{color:var(--white);font-size:16px;line-height:1.4}
.save-item svg{display:block;margin:0 auto 10px}
.savings .btn{margin-top:34px}

/* blogs */
.blogs{height:420px;padding-top:40px;text-align:center}
.blogs h2{font-size:34px;font-weight:700;margin-bottom:30px}
.blog-row{display:flex;justify-content:space-between;text-align:left}
.blog{width:310px}
.blog-img{height:150px}
.blog .date{color:var(--red);font-size:11px;font-weight:700;margin:12px 0 6px}
.blog h4{font-size:14px;line-height:1.4;margin-bottom:10px}
.blog .more{font-size:12px;font-weight:700;color:var(--red);display:flex;align-items:center;gap:10px}
.blog .more i{width:24px;height:24px;border-radius:50%;background:var(--red);display:inline-block}
.blogs .btn-outline{margin-top:26px}

/* partners */
.partners{height:160px;text-align:center}
.partners h2{font-size:34px;font-weight:700;margin-bottom:26px}
.partner-row{display:flex;justify-content:space-between;align-items:center}
.partner-row .logo{width:130px;height:40px;background:#e2e3e7;border-radius:3px}
.partner-row .arrow{width:26px;height:26px;border:1px solid #c9c9ce;border-radius:50%;display:flex;align-items:center;justify-content:center}

/* contact */
.contact{height:540px;background:var(--navy-deep);padding-top:60px;text-align:center}
.contact-photo{position:absolute;inset:0;background:linear-gradient(180deg,#1c2343 0%,#2a3353 60%,#1c2343 100%);opacity:.9}
.contact h2{color:var(--white);font-size:36px;line-height:1.2;font-weight:700;margin-bottom:36px}
.form{width:600px;margin:0 auto;display:grid;grid-template-columns:1fr 1fr;gap:14px;text-align:left}
.field{border-bottom:1px solid #6e7594;color:#c3c7d6;font-size:12px;padding:8px 2px}
.field.full{grid-column:1/3;height:70px}
.contact .btn{margin-top:26px}

/* footer */
.footer{height:268px;padding-top:40px}
.foot-row{display:flex;justify-content:space-between}
.foot-brand .brand{color:var(--navy);font-size:24px}
.foot-col h5{font-size:14px;font-weight:700;margin-bottom:12px}
.foot-col li{list-style:none;font-size:12px;color:var(--muted);line-height:2}
.foot-links{display:grid;grid-template-columns:110px 110px}
.social{display:flex;flex-direction:column;gap:10px}
.social i{display:block;width:28px;height:28px;background:var(--navy)}
.social i.red{background:var(--red)}
.foot-bottom{position:absolute;left:100px;right:100px;bottom:20px;display:flex;justify-content:space-between;font-size:11px;color:var(--muted);border-top:1px solid #e3e3e6;padding-top:14px}
</style>
</head>
<body>

<section class="section hero">
  <div class="hero-photo" role="img" aria-label="Modern home with solar panels on the roof at dusk"></div>
  <div class="wrap">
    <nav class="nav">
      <div class="brand"><span class="brand-square"></span>CORVEL POWER</div>
      <div class="nav-links">
        <span>About Us</span><span>Products</span><span>Residential</span><span>Batteries</span><span>Commercial</span><span>Blog</span><span class="btn">Get a Quote</span>
      </div>
    </nav>
    <div class="hero-copy">
      <div class="tag">Corvel <span>Power</span></div>
      <h1>Australia's top provider of solar power solutions</h1>
      <span class="btn">Contact Us</span>
    </div>
    <div class="hero-dots"><i class="on"></i><i></i><i></i></div>
  </div>
  <svg class="wave" height="220" viewBox="0 0 1200 220" preserveAspectRatio="none" aria-hidden="true">
    <path d="M0 120 C300 220 600 40 1200 20 L1200 220 L0 220Z" fill="var(--red)"/>
    <path d="M0 150 C320 240 620 70 1200 60 L1200 220 L0 220Z" fill="var(--white)"/>
  </svg>
</section>

<section class="section about">
  <div class="wrap">
    <div class="about-photo" role="img" aria-label="House with a tiled roof and palm trees"></div>
    <div class="about-copy">
      <div class="eyebrow">About Us</div>
      <h2>Tailored solutions,<br>fit for you.</h2>
      <p>We understand that every home is different and every household has its own energy needs. Our team designs solar and battery systems around how you live, so you get reliable power, lower bills and a system built to last for years to come.</p>
      <span class="link">More About the Company &rsaquo;</span>
    </div>
  </div>
</section>

<section class="section difference">
  <div class="wrap">
    <h3>The Difference</h3>
    <div class="diff-row">
      <div class="diff-item"><svg width="44" height="44" viewBox="0 0 44 44"><circle cx="22" cy="18" r="10" fill="none" stroke="#d3142b" stroke-width="3"/><path d="M10 40c2-8 22-8 24 0" fill="none" stroke="#d3142b" stroke-width="3"/></svg>Local business</div>
      <div class="diff-item"><svg width="44" height="44" viewBox="0 0 44 44"><rect x="6" y="10" width="32" height="24" fill="none" stroke="#d3142b" stroke-width="3"/><path d="M14 22l6 6 10-12" fill="none" stroke="#d3142b" stroke-width="3"/></svg>15 plus years of customer service</div>
      <div class="diff-item"><svg width="44" height="44" viewBox="0 0 44 44"><path d="M6 22l16-14 16 14v16H6z" fill="none" stroke="#d3142b" stroke-width="3"/><path d="M16 28l5 5 8-10" fill="none" stroke="#d3142b" stroke-width="3"/></svg>Our own certified and skilled installation team</div>
      <div class="diff-item"><svg width="44" height="44" viewBox="0 0 44 44"><circle cx="22" cy="22" r="16" fill="none" stroke="#d3142b" stroke-width="3"/><path d="M22 12v10l7 5" fill="none" stroke="#d3142b" stroke-width="3"/></svg>Trusted leading brands, combining top-grade technology</div>
      <div class="diff-item"><svg width="44" height="44" viewBox="0 0 44 44"><path d="M8 30a14 14 0 0 1 28 0" fill="none" stroke="#d3142b" stroke-width="3"/><rect x="6" y="28" width="7" height="10" fill="#d3142b"/><rect x="31" y="28" width="7" height="10" fill="#d3142b"/></svg>Responsive and quick quality customer service</div>
    </div>
  </div>
  <div class="diff-mark" aria-hidden="true"></div>
  <svg class="wave" height="130" viewBox="0 0 1200 130" preserveAspectRatio="none" aria-hidden="true">
    <path d="M0 40 C400 140 800 0 1200 50 L1200 130 L0 130Z" fill="var(--red)"/>
    <path d="M0 70 C400 160 800 30 1200 80 L1200 130 L0 130Z" fill="var(--light)"/>
  </svg>
</section>

<section class="section ev">
  <div class="wrap">
    <div class="ev-copy">
      <div class="eyebrow">EV Chargers Section</div>
      <h2>Lorem Ipsum is simply dummy printing</h2>
      <p>Charge your electric vehicle at home with power straight from your own roof. We supply and install smart wall chargers that work with your solar and battery system, so every drive costs less and runs on clean energy you made yourself.</p>
      <span class="btn-outline">Discover More &rsaquo;</span>
    </div>
    <div class="ev-photo" role="img" aria-label="Electric vehicle charging stations in a car park"></div>
  </div>
</section>

<section class="section packages">
  <div class="wrap">
    <div class="pkg-head"><h2>Corvel energy packages</h2><span class="btn-outline">More Offers &rsaquo;</span></div>
    <div class="pkg-row">
      <div class="pkg">
        <svg class="house" width="300" height="400" viewBox="0 0 300 400" aria-hidden="true"><path d="M150 4 L296 110 V396 H4 V110Z" fill="#fff" stroke="#dcdce0" stroke-width="2"/><path d="M20 110 L150 16 L280 110" fill="none" stroke="var(--red)" stroke-width="3"/></svg>
        <div class="pkg-img" role="img" aria-label="Solar inverter and battery unit"></div>
        <div class="pkg-price"><span>from<br>$999</span></div>
        <div class="pkg-info"><b>6.6kW Solar Package</b>Premium panels with inverter<span class="was">WAS $4,999 &middot; Save today</span><span class="btn-outline">View Details</span></div>
      </div>
      <div class="pkg">
        <svg class="house" width="300" height="400" viewBox="0 0 300 400" aria-hidden="true"><path d="M150 4 L296 110 V396 H4 V110Z" fill="#fff" stroke="#dcdce0" stroke-width="2"/><path d="M20 110 L150 16 L280 110" fill="none" stroke="var(--red)" stroke-width="3"/></svg>
        <div class="pkg-img" role="img" aria-label="Solar inverter and battery unit"></div>
        <div class="pkg-price"><span>from<br>$999</span></div>
        <div class="pkg-info"><b>10kW Solar Package</b>Panels, inverter and monitoring<span class="was">WAS $6,999 &middot; Save today</span><span class="btn-outline">View Details</span></div>
      </div>
      <div class="pkg">
        <svg class="house" width="300" height="400" viewBox="0 0 300 400" aria-hidden="true"><path d="M150 4 L296 110 V396 H4 V110Z" fill="#fff" stroke="#dcdce0" stroke-width="2"/><path d="M20 110 L150 16 L280 110" fill="none" stroke="var(--red)" stroke-width="3"/></svg>
        <div class="pkg-img" role="img" aria-label="Solar inverter and battery unit"></div>
        <div class="pkg-price"><span>from<br>$999</span></div>
        <div class="pkg-info"><b>Solar &amp; Battery Package</b>Complete home energy system<span class="was">WAS $12,999 &middot; Save today</span><span class="btn-outline">View Details</span></div>
      </div>
    </div>
  </div>
</section>

<section class="section savings">
  <div class="wrap">
    <h2>Watch your savings grow.</h2>
    <p>With rising electricity costs, more Australian homes are turning to solar to take control of their power bills. A well designed system pays for itself over time, adds value to your property and keeps working quietly on your roof every single day.</p>
    <p style="margin-top:14px">Our friendly team will guide you from your first quote through to installation and aftercare, so you always know what you are getting.</p>
    <div class="save-grid">
      <div class="save-item"><svg width="44" height="44" viewBox="0 0 44 44"><circle cx="22" cy="22" r="8" fill="none" stroke="#d3142b" stroke-width="3"/><path d="M22 4v6M22 34v6M4 22h6M34 22h6M9 9l4 4M31 31l4 4M9 35l4-4M31 13l4-4" stroke="#d3142b" stroke-width="3"/></svg>Reduce costs, grow your<br>business</div>
      <div class="save-item"><svg width="44" height="44" viewBox="0 0 44 44"><path d="M6 26l16-14 16 14" fill="none" stroke="#d3142b" stroke-width="3"/><path d="M24 20l-6 10h8l-6 10" fill="none" stroke="#fff" stroke-width="3"/></svg>Avoid blackouts,<br>go off-grid</div>
      <div class="save-item"><svg width="44" height="44" viewBox="0 0 44 44"><path d="M22 6c10 10 12 18 0 32C10 24 12 16 22 6z" fill="none" stroke="#d3142b" stroke-width="3"/></svg>Go solar, eliminate<br>fuel cost</div>
      <div class="save-item"><svg width="44" height="44" viewBox="0 0 44 44"><circle cx="22" cy="22" r="16" fill="none" stroke="#fff" stroke-width="3"/><path d="M22 12v20M27 16h-7a3 3 0 0 0 0 6h4a3 3 0 0 1 0 6h-7" fill="none" stroke="#d3142b" stroke-width="3"/></svg>Save money for<br>your family</div>
    </div>
    <span class="btn">Get Started</span>
  </div>
  <svg class="wave" height="120" viewBox="0 0 1200 120" preserveAspectRatio="none" aria-hidden="true">
    <path d="M0 30 C400 130 800 0 1200 40 L1200 120 L0 120Z" fill="var(--red)"/>
    <path d="M0 60 C400 150 800 30 1200 70 L1200 120 L0 120Z" fill="var(--white)"/>
  </svg>
</section>

<section class="section blogs">
  <div class="wrap">
    <h2>Recent blogs</h2>
    <div class="blog-row">
      <div class="blog"><div class="blog-img" role="img" aria-label="House roof with solar panels" style="background:linear-gradient(180deg,#7fb2db,#3b5579)"></div><div class="date">12 MAY 2024</div><h4>How to size a solar system for your home and family</h4><span class="more">Read More <i></i></span></div>
      <div class="blog"><div class="blog-img" role="img" aria-label="Apartment building with rooftop solar" style="background:linear-gradient(180deg,#9fc6e5,#c7ccd2)"></div><div class="date">28 APR 2024</div><h4>Five ways home batteries keep the lights on</h4><span class="more">Read More <i></i></span></div>
      <div class="blog"><div class="blog-img" role="img" aria-label="Solar panel field at sunset" style="background:linear-gradient(180deg,#e7a15a,#2f3a55)"></div><div class="date">09 APR 2024</div><h4>What rebates can you claim on solar this year</h4><span class="more">Read More <i></i></span></div>
    </div>
    <span class="btn-outline">View All</span>
  </div>
</section>

<section class="section partners">
  <div class="wrap">
    <h2>Our partners</h2>
    <div class="partner-row">
      <span class="arrow"><svg width="10" height="10" viewBox="0 0 10 10"><path d="M7 1L3 5l4 4" fill="none" stroke="#d3142b" stroke-width="2"/></svg></span>
      <span class="logo"></span><span class="logo"></span><span class="logo"></span><span class="logo"></span><span class="logo"></span>
      <span class="arrow"><svg width="10" height="10" viewBox="0 0 10 10"><path d="M3 1l4 4-4 4" fill="none" stroke="#d3142b" stroke-width="2"/></svg></span>
    </div>
  </div>
</section>

<section class="section contact">
  <div class="contact-photo" role="img" aria-label="Rooftop solar array under an evening sky"></div>
  <div class="wrap">
    <h2>Get in touch for<br>an obligation free quote.</h2>
    <div class="form">
      <div class="field">Name</div><div class="field">Phone</div>
      <div class="field">Email</div><div class="field">Average power bill</div>
      <div class="field">Suburb</div><div class="field">Postcode</div>
      <div class="field full">Message</div>
    </div>
    <span class="btn">Submit</span>
  </div>
  <svg class="wave" height="110" viewBox="0 0 1200 110" preserveAspectRatio="none" aria-hidden="true">
    <path d="M0 20 C400 120 800 0 1200 30 L1200 110 L0 110Z" fill="var(--red)"/>
    <path d="M0 50 C400 140 800 30 1200 60 L1200 110 L0 110Z" fill="var(--white)"/>
  </svg>
</section>

<footer class="section footer">
  <div class="wrap">
    <div class="foot-row">
      <div class="foot-brand"><div class="brand"><span class="brand-square"></span>CORVEL POWER</div></div>
      <div class="foot-col"><h5>Contact Us</h5><ul><li>(07) 5550 1824</li><li>hello@corvelpower.com.au</li><li>18 Harbourline Drive, Brisbane QLD</li><li>www.corvelpower.com.au</li></ul></div>
      <div class="foot-col"><h5>Quick Links</h5><ul class="foot-links"><li>About</li><li>Commercial</li><li>Products</li><li>Blog</li><li>Residential</li><li>Contact Us</li><li>Batteries</li></ul></div>
      <div class="social"><i></i><i class="red"></i><i></i></div>
    </div>
  </div>
  <div class="foot-bottom"><span>&copy; 2024 Corvel Power. All rights reserved.</span><span>QLD Electrical Contractors Licence No. 00000</span></div>
</footer>

</body>
</html>
```